【表紙要素】

■書籍タイトル
頼りない課長だった僕が十五期続いた欠損の倉庫業者を再生させた方法

■サブタイトル
町工場のための統率術入門

■キャッチコピー1
「灯台守ステップ術」で部下はあなたについてくる

■キャッチコピー2
特別セミナー動画(無料プレゼント)付き
「粗利が倍増する。倉庫業者が今日から使える5つの収益改善フレーム」

■著者
桐島のぶお

■肩書
物流マーケティングコンサルタント
次世代リーダー育成コンサルタント

■書籍の内容
総合物流会社から赤字続きの関連小会社へ出向となった著者が、会社を立て直す中で学んだリーダーシップ論がテーマになっています。原稿も添付いたします。

■ターゲット
運輸会社の経営者・部課長をターゲットとしています。

■デザイン要望
・イラストを入れるとすると、売上が右肩上がりになっているグラフなどのイメージかなと思いってます。もちろん、その他に良いアイデアがあれば採用したいと思います。
・イラストが入っても、文字だけでも、どちらでも構いません。できれば両方のパターンを比較して決めたいと思います。
・タイトルに関しては、「頼りない課長だった僕が」は小さく、「赤字」「黒字化」は目立つようにお願いします。

本の本文の内容が、あまり堅苦しくない、おもしろおかしい要素が含まれていますので、表紙も明るくてポップな感じが気に入りました。
ただし、誠に申し訳ないのですが、急遽、電子書籍のタイトルを変更することになりました。また、表紙の文字数も減らすことにしました。
したがいまして、今回のコンペとは別に、本日中に再発注をかけます。
何卒、ご理解いただき、再度コンペへのご参加をお願いいたします。

ご提案いただき、ありがとうございました。また、原稿を読んで頂き、内容を踏まえた上でデザインを考えていただき、大変感謝しています。
いろいろと考えた結果、急遽、電子書籍のタイトルを変更することになりました。今回のコンペとは別に、再度依頼をかけますので、またコンペにご参加いただけますようお願いいたします。

```html
<!DOCTYPE html>
<html lang="ja">
<head>
<meta charset="utf-8">
<title>頼りない課長だった僕が十五期続いた欠損の倉庫業者を再生させた方法</title>
<link rel="stylesheet" href="https://fonts.googleapis.com/css2?family=Noto+Serif+JP:wght@500;700;900&family=Noto+Sans+JP:wght@500;700&display=swap">
<style>
  :root {
    --paper: #ffffff;
    --ink: #1b1b1b;
    --accent-red: #d8141c;
    --gold: #b7944a;
    --gold-deep: #a8843c;
  }
  * { margin: 0; padding: 0; box-sizing: border-box; }
  html, body { width: 893px; height: 1200px; overflow: hidden; background: var(--paper); }
  .cover {
    position: relative;
    width: 893px;
    height: 1200px;
    background: var(--paper);
    font-family: "Noto Serif JP", serif;
    color: var(--ink);
    overflow: hidden;
  }
  .abs { position: absolute; line-height: 1; white-space: nowrap; }
  .vertical { writing-mode: vertical-rl; text-orientation: upright; }

  .title-lead {
    top: 44px; left: 410px;
    font-size: 38px; font-weight: 700;
    transform: skewX(-10deg);
  }
  .title-run {
    top: 96px; left: 416px;
    font-size: 72px; font-weight: 900; letter-spacing: -1px;
  }
  .title-loss {
    top: 186px; left: 426px;
    font-size: 134px; font-weight: 900;
    color: var(--accent-red); letter-spacing: -4px;
  }
  .title-company {
    top: 136px; left: 336px;
    font-size: 66px; font-weight: 900;
    color: var(--accent-red);
  }
  .title-revive {
    top: 404px; left: 418px;
    font-size: 86px; font-weight: 900; letter-spacing: -1px;
  }
  .title-method {
    top: 506px; left: 704px;
    font-size: 74px; font-weight: 900;
  }

  .gold-rule {
    top: 266px; left: 320px; width: 3px; height: 400px;
    background: var(--gold);
  }
  .subtitle {
    top: 266px; left: 274px;
    font-size: 30px; font-weight: 700;
    color: var(--gold); letter-spacing: 1px;
  }

  .author-label {
    top: 350px; left: 160px;
    font-size: 24px; font-weight: 700;
  }
  .author-name {
    top: 386px; left: 196px;
    font-size: 54px; font-weight: 900; letter-spacing: 4px;
  }

  .credentials {
    top: 484px; left: 346px;
    display: flex; flex-direction: row-reverse; gap: 6px;
    font-size: 15px; font-weight: 500; color: var(--gold-deep);
  }

  .promo {
    top: 786px; left: 300px; width: 560px;
    font-family: "Noto Sans JP", sans-serif; color: var(--ink);
  }
  .promo-lead {
    border: 2px solid var(--gold);
    padding: 12px 14px;
    font-size: 19px; font-weight: 700; line-height: 1;
    white-space: nowrap;
    margin-bottom: 14px;
  }
  .promo-line {
    font-size: 15px; font-weight: 700; line-height: 1;
    white-space: nowrap; margin-bottom: 10px; padding-left: 4px;
  }
</style>
</head>
<body>
  <main class="cover">
    <p class="abs title-lead">頼りない課長だった僕が</p>
    <p class="abs title-run">十五期続いた</p>
    <p class="abs title-loss">欠損の</p>
    <p class="abs vertical title-company">倉庫業者を</p>
    <p class="abs title-revive">再生させた</p>
    <p class="abs title-method">方法</p>

    <div class="abs gold-rule"></div>
    <p class="abs vertical subtitle">町工場のための統率術入門</p>

    <p class="abs vertical author-label">著者</p>
    <p class="abs vertical author-name">桐島のぶお</p>

    <div class="abs credentials">
      <p class="vertical">物流マーケティングコンサルタント</p>
      <p class="vertical">次世代リーダー育成コンサルタント</p>
    </div>

    <section class="abs promo">
      <p class="promo-lead">「灯台守ステップ術」で部下はあなたについてくる</p>
      <p class="promo-line">特別セミナー動画(無料プレゼント)付き</p>
      <p class="promo-line">「粗利が倍増する。倉庫業者が今日から使える5つの収益改善フレーム」</p>
    </section>
  </main>
</body>
</html>
```